Bright Path Flyer Design for Virtual Online Clinic. -5.5 x 8.5 inches (half sheet)

We need a clean, modern flyer design for Bright Path, a new virtual walk-in clinic based in British Columbia. The flyer will be used in libraries, pharmacies, and community centers to help residents easily access primary care through their Bright Path NFC access card.
The flyer will ask a question : NEED A DOCTOR? This should be large and attention grabbing.
The design should clearly feature a Bright Path card image (the access card) as the centerpiece and visually show how patients can use it to book appointments. The tone should feel trustworthy, healthcare-oriented, and community-friendly — clean fonts, clear spacing, and strong readability from a distance.

Side One: This card has the NFC Access Card.
NEED A DOCTOR? (Large Font, Attention Grabbing)
How to Book an Appointment using your Bright Path Card
Step 1: Tap Your Card on Your Phone
Hold your card near the back of your phone.
It will activate automatically — no app needed.
The Bright Path scheduler will open.
Step 2: Schedule Your Appointment
Select your clinical concern.
Choose your time window.
Register (only once).
Confirm your appointment.
Step 3: Relax, we’ll take care of the rest
A doctor will call during your scheduled time.
Once booked, you’ll be able to call our office.
No emails, no texts — just a real person.
It’s that simple.
Side Two:
About Bright Path
Created by Dr. Marcus Ferrigan
Bright Path was founded to make healthcare simple and convenient. Prescription renewals. Common infections. Medical notes. And so much more.
Our doctors can address 120+ health concerns virtually — providing quality care without the waiting room. No waiting rooms. Just real doctors providing real care.
Why Patients Choose Bright Path
Easy access – book and be seen from anywhere in BC.
Effortless booking – tap your Bright Path Card to begin.
Trusted physicians – every visit is with a licensed BC family doctor.
How It Works
Book your visit — choose a time window that fits your day.
Join the queue — you’ll be called when it’s your turn.
Speak directly with your doctor — simple, secure, and stress-free.
Convenient Care for Common Concerns

Additional Details.
Please find the domain to be launched soon. I've attached the NFC card file for review, it is 85.5 mm x 54 mm. The card will be glued to the flyer.
I've attached examples of flyers but they are not the look I am seeking and I am looking for creative solutions.
Thank you!
http://brightpath-example.test/

Adult Patients in British Columbia

Healthcare

• Looking for clean lines, uniform appearance, and high legibility i.e poppins

0054AA
0677BA
7BADD7
CADEEF
E8F1F8

• Need A Doctor?
• Elegant style, not too busy, clear layout.
• Clutter, look cheap - review examples.

```html
<!DOCTYPE html>
<html lang="en">
<head>
<meta charset="utf-8">
<title>Bright Path Flyer</title>
<link href="https://fonts.googleapis.com/css2?family=Poppins:wght@400;500;600;700&display=swap" rel="stylesheet">
<style>
  :root {
    --canvas: #e1e1e1;
    --paper: #ffffff;
    --brand: #0a9be0;
    --brand-deep: #0677ba;
    --band: #0b5f8e;
    --ink: #1a1a1a;
    --ring: #c9ced3;
    --muted: #eeeeee;
  }
  * { margin: 0; padding: 0; box-sizing: border-box; }
  html, body { width: 1200px; height: 768px; overflow: hidden; }
  body { background: var(--canvas); font-family: "Poppins", sans-serif; color: var(--ink); position: relative; }

  .page { position: absolute; top: 121px; width: 406px; height: 526px; background: var(--paper); overflow: hidden; }
  .page--front { left: 182px; }
  .page--back { left: 613px; }
  .footer-band { position: absolute; left: 0; bottom: 0; width: 100%; height: 16px; background: var(--band); }

  /* Front */
  .doctor-photo { position: absolute; inset: 0; background: linear-gradient(160deg, #d6d6d6 0%, #ececec 40%, #cfd8de 100%);
    clip-path: polygon(205px 0, 406px 0, 406px 526px, 265px 526px); }
  .headline-box { position: absolute; left: 0; top: 18px; width: 328px; height: 78px; background: var(--brand); border-radius: 0 10px 10px 0; display: flex; align-items: center; padding-left: 16px; z-index: 2; }
  .headline { color: #fff; font-weight: 700; font-size: 35px; letter-spacing: 0.3px; }
  .headline-tail { position: absolute; left: 0; top: 0; z-index: 1; }
  .booking-title { position: absolute; left: 10px; top: 129px; font-size: 12.5px; font-weight: 700; color: var(--brand); line-height: 1.05; text-transform: uppercase; }
  .step { position: absolute; left: 10px; width: 250px; display: flex; gap: 12px; }
  .step-icon { flex: 0 0 54px; height: 54px; border-radius: 50%; border: 1.5px solid var(--ring); background: #fff; display: flex; align-items: center; justify-content: center; }
  .step-title { color: var(--brand); font-size: 10.3px; font-weight: 500; line-height: 1.25; margin-bottom: 2px; }
  .step-text { font-size: 5.8px; font-weight: 600; line-height: 1.45; }
  .card-slot { position: absolute; left: 13px; top: 399px; width: 162px; height: 102px; border: 1px solid #f0f0f0; background: #fff; display: flex; align-items: center; justify-content: center; }
  .card-slot svg { position: absolute; inset: 0; }
  .card-slot-label { position: relative; color: #e6e6e6; font-size: 11px; font-weight: 500; }

  /* Back */
  .care-photo { position: absolute; left: 0; top: 31px; width: 406px; height: 196px; background: linear-gradient(120deg, #b9c7d3 0%, #e6e2dc 45%, #a99a86 100%); }
  .about-top { position: absolute; left: 0; top: 0; width: 211px; height: 14px; background: var(--brand); }
  .about-box { position: absolute; left: 0; top: 11px; width: 393px; height: 54px; background: var(--brand); border-radius: 0 6px 6px 0; display: flex; align-items: center; justify-content: flex-end; padding-right: 10px; }
  .about-title { color: #fff; font-size: 36px; font-weight: 600; }
  .story { position: absolute; left: 0; top: 226px; width: 210px; height: 284px; background: var(--brand); color: #fff; padding: 15px 13px; }
  .founder { font-size: 15.5px; font-weight: 600; line-height: 1.05; }
  .story-text { font-size: 9.8px; font-weight: 500; line-height: 15.6px; margin-top: 36px; }
  .story-text + .story-text { margin-top: 15px; }
  .feature { position: absolute; left: 199px; width: 205px; }
  .feature-icon { position: absolute; left: 0; top: 0; width: 37px; height: 37px; border-radius: 50%; background: var(--brand); border: 2px solid #fff; box-shadow: 0 0 0 1px var(--brand); display: flex; align-items: center; justify-content: center; }
  .feature-title { margin-left: 45px; color: var(--brand); font-size: 14.5px; font-weight: 600; line-height: 1.15; }
  .feature-list { list-style: none; margin-left: 45px; margin-top: 8px; }
  .feature-list li { position: relative; padding-left: 7px; font-size: 6.3px; font-weight: 600; line-height: 1.3; margin-bottom: 10px; }
  .feature-list li::before { content: ""; position: absolute; left: 0; top: 2.5px; width: 3.5px; height: 3.5px; border-radius: 50%; background: var(--ink); }
</style>
</head>
<body>

<section class="page page--front">
  <div class="doctor-photo" role="img" aria-label="Photo of a smiling doctor in a white coat with a stethoscope, writing on a clipboard"></div>
  <svg class="headline-tail" width="406" height="140" viewBox="0 0 406 140"><polygon points="215,92 328,92 222,124" fill="var(--brand-deep)"/></svg>
  <div class="headline-box"><h1 class="headline">NEED A DOCTOR?</h1></div>

  <h2 class="booking-title">How to book an appointment<br>using your Bright Path card</h2>

  <div class="step" style="top:167px">
    <div class="step-icon">
      <svg width="32" height="32" viewBox="0 0 32 32" fill="none" stroke="var(--brand)" stroke-width="1.6"><rect x="5" y="3" width="13" height="25" rx="2"/><rect x="11" y="9" width="17" height="11" rx="1.5" fill="#fff"/><line x1="14" y1="13" x2="25" y2="13"/><line x1="14" y1="16" x2="22" y2="16"/><line x1="10" y1="25" x2="13" y2="25"/></svg>
    </div>
    <div>
      <p class="step-title">Step 1: Tap Your Card on<br>Your Phone</p>
      <p class="step-text">Hold your card near the back of your phone.<br>It will activate automatically – no app needed.<br>The Bright Path scheduler will open.</p>
    </div>
  </div>

  <div class="step" style="top:236px">
    <div class="step-icon">
      <svg width="34" height="34" viewBox="0 0 34 34" fill="none" stroke="var(--brand)" stroke-width="1.5"><rect x="3" y="6" width="26" height="22" rx="2"/><line x1="3" y1="11" x2="29" y2="11"/><line x1="9" y1="3" x2="9" y2="8"/><line x1="16" y1="3" x2="16" y2="8"/><line x1="23" y1="3" x2="23" y2="8"/><rect x="7" y="14" width="3" height="3"/><rect x="13" y="14" width="3" height="3"/><rect x="19" y="14" width="3" height="3"/><rect x="7" y="20" width="3" height="3"/><rect x="13" y="20" width="3" height="3"/><circle cx="26" cy="26" r="6" fill="#fff"/><polyline points="23,26 25.5,28.5 29,24"/></svg>
    </div>
    <div>
      <p class="step-title">Step 2: Schedule Your<br>Appointment</p>
      <p class="step-text">Select your clinical concern.<br>Choose your time window.<br>Register (only once).<br>Confirm your appointment.</p>
    </div>
  </div>

  <div class="step" style="top:311px">
    <div class="step-icon">
      <svg width="32" height="32" viewBox="0 0 32 32" fill="var(--brand)"><circle cx="11" cy="5" r="3.5"/><path d="M7 10h6l2 9h8l3 10h-3l-2.5-7H12L7 19z"/><path d="M4 14l2 0 2 10h-3z"/></svg>
    </div>
    <div>
      <p class="step-title">Step 3: Relax, we’ll take care<br>of the rest</p>
      <p class="step-text">A doctor will call during your scheduled time.<br>Once booked, you’ll be able to call our office.<br>No emails, no texts – just a real person.<br>It’s that simple.</p>
    </div>
  </div>

  <div class="card-slot">
    <svg width="162" height="102" viewBox="0 0 162 102"><polygon points="0,0 36,0 0,34" fill="var(--muted)"/><polygon points="162,102 126,102 162,66" fill="var(--muted)"/></svg>
    <span class="card-slot-label">CARD SECTION</span>
  </div>

  <div class="footer-band"></div>
</section>

<section class="page page--back">
  <div class="care-photo" role="img" aria-label="Photo of a doctor holding a patient's hand, with a stethoscope"></div>
  <div class="about-top"></div>
  <div class="about-box"><h1 class="about-title">About Bright Path</h1></div>

  <div class="story">
    <h2 class="founder">Created by<br>Dr. Marcus Ferrigan</h2>
    <p class="story-text">Bright Path was founded to make healthcare simple and convenient.<br>Prescription renewals.<br>Common infections.<br>Medical notes.<br>And so much more.</p>
    <p class="story-text">Our doctors can address 120+ health concerns virtually – providing quality care without the waiting room.<br>No waiting rooms.<br>Just real doctors providing real care.</p>
  </div>

  <div class="feature" style="top:235px">
    <div class="feature-icon">
      <svg width="22" height="22" viewBox="0 0 22 22" fill="none" stroke="#fff" stroke-width="1.4"><circle cx="11" cy="9" r="6.5"/><polyline points="8,9 10.3,11.3 14,7"/><polyline points="7,14 5,20 8,18.5 9.5,21 11,16"/><polyline points="15,14 17,20 14,18.5 12.5,21 11,16"/></svg>
    </div>
    <h3 class="feature-title">Why Patients<br>Choose Bright Path</h3>
    <ul class="feature-list">
      <li>Easy access – book and be seen<br>from anywhere in BC.</li>
      <li>Effortless booking – tap your Bright Path<br>Card to begin.</li>
      <li>Trusted physicians – every visit is with<br>a licensed BC family doctor.</li>
    </ul>
  </div>

  <div class="feature" style="top:371px">
    <div class="feature-icon">
      <svg width="22" height="22" viewBox="0 0 22 22" fill="none" stroke="#fff" stroke-width="1.4"><path d="M3 4h6v14H3z"/><path d="M9 4h6v6"/><circle cx="15" cy="15" r="4.5"/><line x1="15" y1="14" x2="15" y2="17"/><line x1="15" y1="12" x2="15" y2="12.3"/></svg>
    </div>
    <h3 class="feature-title" style="padding-top:10px">How It Works</h3>
    <ul class="feature-list" style="margin-top:11px">
      <li>Book your visit – choose a time window<br>that fits your day.</li>
      <li>Join the queue – you’ll be called when<br>it’s your turn.</li>
      <li>Speak directly with your doctor –<br>simple, secure, and stress-free.</li>
      <li>Convenient Care for Common Concerns</li>
    </ul>
  </div>

  <div class="footer-band"></div>
</section>

</body>
</html>
```